TalkWell Needs a Business Card

We need a business card for Tomas Ferreby, Ph.D., CCC-SLP, who is affiliated with Hollander Ridge University. He is an Associate Professor and Licensed Speech-Language Pathologist, Department of Communication Disorders, College of Health and Human Services.

He has a consulting business "TalkWell Consultant". The logo is attached. The consulting company color is Turquoise. HRU school color is orange.

The consulting business focus on: Consultation, Research & Professional Development. Our target market is individuals with annual family income of $100,000.00 or more for consultation and speech-language pathologists for professional development activities.

No harsh colors, subtle colors appreciated. Address, e-mail, telephone, and small scan logo for a link to our website. Creativity in design will be appreciated. Please add your comments, why you created this design?

Thanks and looking for submissions.

```html
<!DOCTYPE html>
<html lang="en">
<head>
<meta charset="utf-8">
<title>TalkWell Consultant – Business Card</title>
<link rel="stylesheet" href="https://fonts.googleapis.com/css2?family=Exo+2:wght@400;500;600&display=swap">
<style>
  :root {
    --backdrop: #e9e7e3;
    --card: #ffffff;
    --turquoise: #5fc9d3;
    --leaf: #62b84a;
    --orange: #eea35a;
    --ink: #2b2b2b;
    --ink-soft: #555555;
    --shadow: rgba(0, 0, 0, 0.16);
  }
  * { margin: 0; padding: 0; box-sizing: border-box; }
  html, body {
    width: 1057px;
    height: 1200px;
    overflow: hidden;
    background: var(--backdrop);
    font-family: "Exo 2", "Helvetica Neue", Arial, sans-serif;
    color: var(--ink);
  }
  .sheet { position: relative; width: 1057px; height: 1200px; }
  .card {
    position: absolute;
    top: 215px;
    width: 440px;
    height: 770px;
    background: var(--card);
    box-shadow: 0 14px 34px var(--shadow);
  }
  .card--front { left: 60px; }
  .card--back { left: 557px; }

  /* brand lockup */
  .brand { display: flex; align-items: center; gap: 12px; }
  .brand__dot {
    width: 40px; height: 40px;
    border-radius: 50%;
    background: var(--turquoise);
    flex: none;
  }
  .brand__name {
    font-weight: 500;
    color: var(--turquoise);
    letter-spacing: 0.5px;
    white-space: nowrap;
  }
  .card--front .brand { position: absolute; top: 58px; right: 56px; }
  .card--front .brand__name { font-size: 24px; }

  /* side band */
  .band { position: absolute; right: 0; width: 34px; }
  .band--turquoise { top: 0; height: 300px; background: var(--turquoise); }
  .band--leaf { top: 300px; height: 180px; background: var(--leaf); }
  .band--orange { top: 480px; height: 8px; background: var(--orange); }
  .band__icon { position: absolute; left: 8px; width: 18px; height: 18px; }

  /* identity */
  .identity {
    position: absolute;
    top: 168px;
    right: 56px;
    text-align: right;
  }
  .identity__name { font-size: 30px; font-weight: 600; letter-spacing: 1.5px; line-height: 1.2; }
  .identity__credentials {
    margin-top: 2px;
    font-size: 14px;
    font-weight: 500;
    letter-spacing: 1px;
    color: var(--ink-soft);
  }
  .identity__rule {
    width: 60px;
    height: 3px;
    margin: 10px 0 8px auto;
    background: var(--orange);
  }
  .identity__role {
    font-size: 12px;
    font-weight: 500;
    letter-spacing: 1px;
    color: var(--ink-soft);
    line-height: 1.5;
  }
  .identity__affiliation {
    font-size: 13px;
    font-weight: 600;
    letter-spacing: 0.5px;
    color: var(--orange);
    line-height: 1.5;
  }

  /* contact lines */
  .contact {
    position: absolute;
    right: 56px;
    font-size: 15px;
    color: var(--ink-soft);
    text-align: right;
    letter-spacing: 0.5px;
  }
  .contact--phone { top: 322px; }
  .contact--mobile { top: 362px; }
  .contact--email { top: 402px; }
  .contact--web { top: 442px; }

  /* address */
  .address {
    position: absolute;
    left: 40px;
    bottom: 70px;
    font-size: 20px;
    font-weight: 500;
    font-style: normal;
    line-height: 1.45;
    letter-spacing: 0.8px;
  }

  /* back */
  .card--back .brand {
    position: absolute;
    top: 50%;
    left: 50%;
    transform: translate(-50%, -50%);
  }
  .card--back .brand__dot { width: 52px; height: 52px; }
  .card--back .brand__name { font-size: 30px; }
  .scan {
    position: absolute;
    left: 50%;
    bottom: 70px;
    width: 84px;
    height: 84px;
    transform: translateX(-50%);
    background: var(--card);
    border: 6px solid var(--orange);
    outline: 18px solid #f3f3f3;
    outline-offset: -30px;
  }
</style>
</head>
<body>
<main class="sheet">

  <section class="card card--front" aria-label="Business card front">
    <div class="brand">
      <span class="brand__dot"></span>
      <span class="brand__name">TalkWell Consultant</span>
    </div>

    <div class="band band--turquoise"></div>
    <div class="band band--leaf">
      <svg class="band__icon" style="top:24px" viewBox="0 0 24 24" aria-hidden="true">
        <path fill="#fff" d="M6.6 10.8c1.4 2.8 3.8 5.1 6.6 6.6l2.2-2.2c.3-.3.7-.4 1-.2 1.1.4 2.3.6 3.6.6.6 0 1 .4 1 1V20c0 .6-.4 1-1 1C10.6 21 3 13.4 3 4c0-.6.4-1 1-1h3.5c.6 0 1 .4 1 1 0 1.3.2 2.5.6 3.6.1.3 0 .7-.2 1L6.6 10.8z"/>
      </svg>
      <svg class="band__icon" style="top:64px" viewBox="0 0 24 24" aria-hidden="true">
        <rect x="6" y="2" width="12" height="20" rx="2" fill="#fff"/>
        <rect x="8" y="5" width="8" height="12" fill="var(--leaf)"/>
      </svg>
      <svg class="band__icon" style="top:104px" viewBox="0 0 24 24" aria-hidden="true">
        <rect x="2" y="5" width="20" height="14" rx="1.5" fill="#fff"/>
        <path d="M3 6l9 7 9-7" fill="none" stroke="var(--leaf)" stroke-width="1.8"/>
      </svg>
      <svg class="band__icon" style="top:144px" viewBox="0 0 24 24" aria-hidden="true">
        <circle cx="12" cy="12" r="9" fill="#fff"/>
        <path d="M3 12h18M12 3c3 3 3 15 0 18M12 3c-3 3-3 15 0 18" fill="none" stroke="var(--leaf)" stroke-width="1.4"/>
      </svg>
    </div>
    <div class="band band--orange"></div>

    <div class="identity">
      <p class="identity__name">TOMAS FERREBY</p>
      <p class="identity__credentials">Ph.D., CCC-SLP</p>
      <div class="identity__rule"></div>
      <p class="identity__role">ASSOCIATE PROFESSOR</p>
      <p class="identity__affiliation">Hollander Ridge University</p>
    </div>

    <p class="contact contact--phone">012 555 0147</p>
    <p class="contact contact--mobile">012 555 0148</p>
    <p class="contact contact--email">tomas@talkwell.example</p>
    <p class="contact contact--web">www.talkwell.example</p>

    <address class="address">
      214 Maple Court Road,<br>
      2nd building Street West
    </address>
  </section>

  <section class="card card--back" aria-label="Business card back">
    <div class="brand">
      <span class="brand__dot"></span>
      <span class="brand__name">TalkWell Consultant</span>
    </div>
    <div class="scan" role="img" aria-label="Website scan code area"></div>
  </section>

</main>
</body>
</html>
```